Design of labels for exciting new natural skincare products...natural deodorant

I need some labels designed for a range of natural skincare, initially a natural deodorant paste. i will be offering a range of fragrances so i want a basic idea that i can drop different colours / ingredients into easily.

Fragrances are:
1. Jasmine, Orange and Bergamot
2. Lavender & Bergamot
3. Peppermint & Tea tree
4. Unscented
5. Lime, Lemongrass & Ginger

I am a new startup and will be selling online and through a couple of specialty online stores. The final design should encompass our ethos which is clean and green, not fussy nor clinical but friendly and easily accessible. I like fresh, contemporary modern look referencing vintage aesthetics.

The idea is that these products are better for your body AND the environment, and we pledge to use no plastic to package or distribute our products. i like the use of contemporary pastels such as soft pinks, tans and green/blue/aquas, though am open to new ideas too. the logo (attached) appears in red but that should not necessarily be used. i also like black and white with touches of colour.

Target Market(s)

Eco aware, health concious consumers with a reasonable skincare budget.

Industry/Entity Type

Skin Care Product

Font styles to use
Serif
Sans Serif
Decorative

Colors
2eb6a2
b768aa
eea4c8
fabb94
85cae6
cfeae6
eaf2ce
000000
eaeaea

Requirements
Must have
• Labels are for a small glass jar - the dimensions are 2cm high only and wrapping around the jar - at least 10cm wide. i'm also going to be providing a smaller size so this needs to be able to scale down to 1.5cm high and 8cm wide.
• the logo (supplied)
• title: Natural Deodorant
• Subtitle: Orange, Jasmine & Bergamot
• 45g
• Ingredients: tapioca starch*, bicarbonate of soda, Coconut oil*, shea butter*, mango butter*, diatomaceous earth*, sweet almond oil*, vitamin e*, tea tree oil*, Sweet orange essential oil*, Jasmine essential oil*, Bergamot essential oil*.
• *Certified organic ingredient
• (DESIGNERS - PLEASE NOTE NOT ALL THE INGREDIENTS ARE ORGANIC, PLEASE LIST THEM WITH A STAR * IF I HAVE SUPPLIED IT, THEN *Certified organic ingredient BELOW IN SLIGHTLY SMALLER TEXT - THIS SERVES AS THE KEY FOR THE INGREDIENTS LIST)
• pebblewick.nz
• Massage a pea-sized amount onto clean, dry armpits for an odour-free day.
• If irritation develops discontinue use and contact Fern Hollow. (please italicise the company name)
Nice to have
• open to ideas - i am attaching some examples of designs i like, you'll notice i swing between plain black and white aesthetics and a more decorative look. In general i like the old "medicine bottle" look, with hand sketched illustrations. But i'm open to ideas!

```html
<!DOCTYPE html>
<html lang="en">
<head>
<meta charset="utf-8">
<title>Fern Hollow Natural Deodorant – Label Range</title>
<link rel="stylesheet" href="https://fonts.googleapis.com/css2?family=Arimo:wght@400;700&family=Fira+Sans+Extra+Condensed:wght@400;500;700&display=swap">
<style>
  :root{
    --page:#000000;
    --white:#ffffff;
    --brand-red:#e3262c;
    --title-teal:#2eb6a2;
    --ring-green:#8cc63f;
    --badge-green:#4d873a;
    --ink:#1a1a1a;
    --icon-grey:#3f3f3f;
    --weight-grey:#333333;
  }
  *{box-sizing:border-box;margin:0;padding:0}
  html,body{width:993px;height:1200px;overflow:hidden;background:var(--page)}
  .range{position:relative;width:993px;height:1200px;padding:60px 46px;display:flex;flex-direction:column;gap:45px}

  .label{position:relative;width:900px;height:180px;background:var(--bg);overflow:hidden;
    font-family:"Fira Sans Extra Condensed",sans-serif;color:var(--ink)}
  .label--orange{--bg:#f8e0a6;--band:#f5961e;--accent:#f5961e}
  .label--lavender{--bg:#fbe0ea;--band:#b768aa;--accent:#b768aa}
  .label--peppermint{--bg:#d8ecea;--band:#1fae6c;--accent:#1fae6c}
  .label--unscented{--bg:#d4ecf9;--band:#27c0ec;--accent:#2eb6a2}
  .label--lime{--bg:#fbf8d8;--band:#8cc63f;--accent:#7cb82f}

  .label__band{position:absolute;left:0;right:0;bottom:0;height:30px;background:var(--band)}
  .label__info{position:absolute;left:14px;top:12px;width:252px;font-size:13.4px;line-height:16px}
  .label__info strong{font-weight:700}
  .label__info p + p{margin-top:9px}
  .label__key{position:absolute;left:14px;bottom:8px;font-size:12px;color:var(--white)}
  .label__web{position:absolute;right:26px;bottom:7px;font-family:"Arimo",sans-serif;font-size:14.5px;color:var(--white)}

  .label__disc{position:absolute;left:0;top:0}
  .label__front{position:absolute;left:290px;width:254px;text-align:center}
  .brand-name{top:28px;font-weight:700;font-size:46px;line-height:48px;color:var(--brand-red);letter-spacing:-.5px}
  .product-title{top:96px;font-weight:400;font-size:33px;line-height:36px;color:var(--title-teal)}
  .product-variant{top:134px;display:flex;justify-content:center;align-items:center;gap:6px}
  .product-variant__scent{font-size:15px;line-height:16px;color:var(--accent);text-align:right}
  .product-variant__rule{width:2px;height:30px;background:var(--accent)}
  .product-variant__weight{font-size:32px;line-height:32px;color:var(--weight-grey)}

  .label__seal{position:absolute;left:590px;top:0}
  .claim{position:absolute;font-family:"Arimo",sans-serif;font-weight:700;font-size:10px;line-height:10px;color:var(--icon-grey);text-transform:uppercase}
  .claim--cruelty{left:694px;top:53px}
  .claim--nz{left:703px;top:113px}
  .icon-slot{position:absolute;background:#6b6b6b;border-radius:40% 50% 30% 40%}
  .icon-slot--rabbit{left:708px;top:14px;width:50px;height:36px}
  .icon-slot--kiwi{left:708px;top:80px;width:56px;height:32px}
  .label__icons{position:absolute;left:770px;top:20px}
</style>
</head>
<body>
<main class="range">

  <!-- shared front panel pieces repeated per fragrance -->
  <section class="label label--orange">
    <div class="label__band"></div>
    <div class="label__info">
      <p><strong>Ingredients:</strong> Coconut oil*, tapioca starch*, bicarbonate of soda, shea butter*, mango butter*, diatomaceous earth*, sweet almond oil*, vitamin e*, tea tree oil*, Sweet orange essential oil*, Jasmine essential oil*, Bergamot essential oil*.</p>
      <p><strong>To use:</strong> Massage a pea sized amount onto clean, dry underarms for an odour-free day.</p>
    </div>
    <span class="label__key">*certified organic ingredient</span>
    <svg class="label__disc" width="900" height="180" aria-hidden="true"><circle cx="417" cy="122" r="128" fill="#fff"/><circle cx="417" cy="122" r="108" fill="none" stroke="#8cc63f" stroke-width="3"/></svg>
    <div class="label__front brand-name">Fern Hollow</div>
    <div class="label__front product-title">Natural Deodorant</div>
    <div class="label__front product-variant"><span class="product-variant__scent">Orange, Jasmine<br>&amp; Bergamot</span><span class="product-variant__rule"></span><span class="product-variant__weight">50g</span></div>
    <svg class="label__seal" width="64" height="140" aria-hidden="true"><path d="M4 0H64V136L34 120L4 136Z" fill="#4d873a"/><circle cx="34" cy="75" r="42" fill="#4d873a"/><circle cx="34" cy="75" r="35" fill="none" stroke="#fff" stroke-width="2"/></svg>
    <div class="icon-slot icon-slot--rabbit" role="img" aria-label="Rabbit icon for cruelty-free claim"></div>
    <span class="claim claim--cruelty">Not tested<br>on animals</span>
    <div class="icon-slot icon-slot--kiwi" role="img" aria-label="Kiwi bird icon for New Zealand made"></div>
    <span class="claim claim--nz">New<br>Zealand<br>Made</span>
    <svg class="label__icons" width="60" height="130" aria-hidden="true"><circle cx="28" cy="27" r="25" fill="#3f3f3f"/><circle cx="28" cy="27" r="20" fill="none" stroke="#fff" stroke-width="2"/><circle cx="28" cy="97" r="25" fill="#3f3f3f"/><path d="M18 104a12 12 0 1 1 18 3" fill="none" stroke="#fff" stroke-width="5"/><path d="M30 110l10-10 4 13z" fill="#fff"/></svg>
    <span class="label__web">www.website.com</span>
  </section>

  <section class="label label--lavender">
    <div class="label__band"></div>
    <div class="label__info">
      <p><strong>Ingredients:</strong> Coconut oil*, tapioca starch*, bicarbonate of soda, shea butter*, mango butter*, diatomaceous earth*, sweet almond oil*, vitamin e*, tea tree oil*, Sweet orange essential oil*, Jasmine essential oil*, Bergamot essential oil*.</p>
      <p><strong>To use:</strong> Massage a pea sized amount onto clean, dry underarms for an odour-free day.</p>
    </div>
    <span class="label__key">*certified organic ingredient</span>
    <svg class="label__disc" width="900" height="180" aria-hidden="true"><circle cx="417" cy="122" r="128" fill="#fff"/><circle cx="417" cy="122" r="108" fill="none" stroke="#8cc63f" stroke-width="3"/></svg>
    <div class="label__front brand-name">Fern Hollow</div>
    <div class="label__front product-title">Natural Deodorant</div>
    <div class="label__front product-variant"><span class="product-variant__scent">Lavender<br>&amp; Bergamot</span><span class="product-variant__rule"></span><span class="product-variant__weight">50g</span></div>
    <svg class="label__seal" width="64" height="140" aria-hidden="true"><path d="M4 0H64V136L34 120L4 136Z" fill="#4d873a"/><circle cx="34" cy="75" r="42" fill="#4d873a"/><circle cx="34" cy="75" r="35" fill="none" stroke="#fff" stroke-width="2"/></svg>
    <div class="icon-slot icon-slot--rabbit" role="img" aria-label="Rabbit icon for cruelty-free claim"></div>
    <span class="claim claim--cruelty">Not tested<br>on animals</span>
    <div class="icon-slot icon-slot--kiwi" role="img" aria-label="Kiwi bird icon for New Zealand made"></div>
    <span class="claim claim--nz">New<br>Zealand<br>Made</span>
    <svg class="label__icons" width="60" height="130" aria-hidden="true"><circle cx="28" cy="27" r="25" fill="#3f3f3f"/><circle cx="28" cy="27" r="20" fill="none" stroke="#fff" stroke-width="2"/><circle cx="28" cy="97" r="25" fill="#3f3f3f"/><path d="M18 104a12 12 0 1 1 18 3" fill="none" stroke="#fff" stroke-width="5"/><path d="M30 110l10-10 4 13z" fill="#fff"/></svg>
    <span class="label__web">www.website.com</span>
  </section>

  <section class="label label--peppermint">
    <div class="label__band"></div>
    <div class="label__info">
      <p><strong>Ingredients:</strong> Coconut oil*, tapioca starch*, bicarbonate of soda, shea butter*, mango butter*, diatomaceous earth*, sweet almond oil*, vitamin e*, tea tree oil*, Sweet orange essential oil*, Jasmine essential oil*, Bergamot essential oil*.</p>
      <p><strong>To use:</strong> Massage a pea sized amount onto clean, dry underarms for an odour-free day.</p>
    </div>
    <span class="label__key">*certified organic ingredient</span>
    <svg class="label__disc" width="900" height="180" aria-hidden="true"><circle cx="417" cy="122" r="128" fill="#fff"/><circle cx="417" cy="122" r="108" fill="none" stroke="#8cc63f" stroke-width="3"/></svg>
    <div class="label__front brand-name">Fern Hollow</div>
    <div class="label__front product-title">Natural Deodorant</div>
    <div class="label__front product-variant"><span class="product-variant__scent">Peppermint<br>&amp; Tea tree</span><span class="product-variant__rule"></span><span class="product-variant__weight">50g</span></div>
    <svg class="label__seal" width="64" height="140" aria-hidden="true"><path d="M4 0H64V136L34 120L4 136Z" fill="#4d873a"/><circle cx="34" cy="75" r="42" fill="#4d873a"/><circle cx="34" cy="75" r="35" fill="none" stroke="#fff" stroke-width="2"/></svg>
    <div class="icon-slot icon-slot--rabbit" role="img" aria-label="Rabbit icon for cruelty-free claim"></div>
    <span class="claim claim--cruelty">Not tested<br>on animals</span>
    <div class="icon-slot icon-slot--kiwi" role="img" aria-label="Kiwi bird icon for New Zealand made"></div>
    <span class="claim claim--nz">New<br>Zealand<br>Made</span>
    <svg class="label__icons" width="60" height="130" aria-hidden="true"><circle cx="28" cy="27" r="25" fill="#3f3f3f"/><circle cx="28" cy="27" r="20" fill="none" stroke="#fff" stroke-width="2"/><circle cx="28" cy="97" r="25" fill="#3f3f3f"/><path d="M18 104a12 12 0 1 1 18 3" fill="none" stroke="#fff" stroke-width="5"/><path d="M30 110l10-10 4 13z" fill="#fff"/></svg>
    <span class="label__web">www.website.com</span>
  </section>

  <section class="label label--unscented">
    <div class="label__band"></div>
    <div class="label__info">
      <p><strong>Ingredients:</strong> Coconut oil*, tapioca starch*, bicarbonate of soda, shea butter*, mango butter*, diatomaceous earth*, sweet almond oil*, vitamin e*, tea tree oil*, Sweet orange essential oil*, Jasmine essential oil*, Bergamot essential oil*.</p>
      <p><strong>To use:</strong> Massage a pea sized amount onto clean, dry underarms for an odour-free day.</p>
    </div>
    <span class="label__key">*certified organic ingredient</span>
    <svg class="label__disc" width="900" height="180" aria-hidden="true"><circle cx="417" cy="122" r="128" fill="#fff"/><circle cx="417" cy="122" r="108" fill="none" stroke="#8cc63f" stroke-width="3"/></svg>
    <div class="label__front brand-name">Fern Hollow</div>
    <div class="label__front product-title">Natural Deodorant</div>
    <div class="label__front product-variant"><span class="product-variant__scent" style="font-size:18px">Unscented</span><span class="product-variant__rule"></span><span class="product-variant__weight">50g</span></div>
    <svg class="label__seal" width="64" height="140" aria-hidden="true"><path d="M4 0H64V136L34 120L4 136Z" fill="#4d873a"/><circle cx="34" cy="75" r="42" fill="#4d873a"/><circle cx="34" cy="75" r="35" fill="none" stroke="#fff" stroke-width="2"/></svg>
    <div class="icon-slot icon-slot--rabbit" role="img" aria-label="Rabbit icon for cruelty-free claim"></div>
    <span class="claim claim--cruelty">Not tested<br>on animals</span>
    <div class="icon-slot icon-slot--kiwi" role="img" aria-label="Kiwi bird icon for New Zealand made"></div>
    <span class="claim claim--nz">New<br>Zealand<br>Made</span>
    <svg class="label__icons" width="60" height="130" aria-hidden="true"><circle cx="28" cy="27" r="25" fill="#3f3f3f"/><circle cx="28" cy="27" r="20" fill="none" stroke="#fff" stroke-width="2"/><circle cx="28" cy="97" r="25" fill="#3f3f3f"/><path d="M18 104a12 12 0 1 1 18 3" fill="none" stroke="#fff" stroke-width="5"/><path d="M30 110l10-10 4 13z" fill="#fff"/></svg>
    <span class="label__web">www.website.com</span>
  </section>

  <section class="label label--lime">
    <div class="label__band"></div>
    <div class="label__info">
      <p><strong>Ingredients:</strong> Coconut oil*, tapioca starch*, bicarbonate of soda, shea butter*, mango butter*, diatomaceous earth*, sweet almond oil*, vitamin e*, tea tree oil*, Sweet orange essential oil*, Jasmine essential oil*, Bergamot essential oil*.</p>
      <p><strong>To use:</strong> Massage a pea sized amount onto clean, dry underarms for an odour-free day.</p>
    </div>
    <span class="label__key">*certified organic ingredient</span>
    <svg class="label__disc" width="900" height="180" aria-hidden="true"><circle cx="417" cy="122" r="128" fill="#fff"/><circle cx="417" cy="122" r="108" fill="none" stroke="#8cc63f" stroke-width="3"/></svg>
    <div class="label__front brand-name">Fern Hollow</div>
    <div class="label__front product-title">Natural Deodorant</div>
    <div class="label__front product-variant"><span class="product-variant__scent">Lime, Lemongrass<br>&amp; Ginger</span><span class="product-variant__rule"></span><span class="product-variant__weight">50g</span></div>
    <svg class="label__seal" width="64" height="140" aria-hidden="true"><path d="M4 0H64V136L34 120L4 136Z" fill="#4d873a"/><circle cx="34" cy="75" r="42" fill="#4d873a"/><circle cx="34" cy="75" r="35" fill="none" stroke="#fff" stroke-width="2"/></svg>
    <div class="icon-slot icon-slot--rabbit" role="img" aria-label="Rabbit icon for cruelty-free claim"></div>
    <span class="claim claim--cruelty">Not tested<br>on animals</span>
    <div class="icon-slot icon-slot--kiwi" role="img" aria-label="Kiwi bird icon for New Zealand made"></div>
    <span class="claim claim--nz">New<br>Zealand<br>Made</span>
    <svg class="label__icons" width="60" height="130" aria-hidden="true"><circle cx="28" cy="27" r="25" fill="#3f3f3f"/><circle cx="28" cy="27" r="20" fill="none" stroke="#fff" stroke-width="2"/><circle cx="28" cy="97" r="25" fill="#3f3f3f"/><path d="M18 104a12 12 0 1 1 18 3" fill="none" stroke="#fff" stroke-width="5"/><path d="M30 110l10-10 4 13z" fill="#fff"/></svg>
    <span class="label__web">www.website.com</span>
  </section>

</main>
</body>
</html>
```